Website Online Research Solutions

We are a small European high-tech online research company.
With our own state of the art software we run online panels and are conducting reseach for companies. Partly research via our own panel and partly via panels we maintain for our customers.
Our current website is old and outdatet: www.pravelo.nl.
We are in the process to change the content of the site. We want a modern, european and businesslike design for our new website.
Our logo has to stay the same (left uppersite of our website and attached) but can be changed a little to adapt it to the new design of the website. The colors of the site are up to you.
Target Market(s)
Marketeers and researchers of large and middle size companies in all kind of fields.
Industry/Entity Type
Online
Look and feel
Each slider illustrates characteristics of the customer's brand and the style your logo design should communicate.

```html
<!DOCTYPE html>
<html lang="nl">
<head>
<meta charset="utf-8">
<title>Pravelo – Online Research Solutions</title>
<link href="https://fonts.googleapis.com/css2?family=Alfa+Slab+One&family=Arimo:wght@400;700&family=Didact+Gothic&family=Noto+Sans:wght@400;700&display=swap" rel="stylesheet">
<style>
:root{
  --dark:#333333;
  --nav:#8a8a8a;
  --frame:#888888;
  --white:#ffffff;
  --red:#e01a1a;
  --text:#222222;
  --muted:#b9b9b9;
  --panel:#e4e4e4;
  --field:#dcdcdc;
  --green:#1f7a3a;
  --blue:#2763a8;
  --olive:#7a6a1a;
}
*{margin:0;padding:0;box-sizing:border-box}
html,body{width:1200px;height:1101px;overflow:hidden;background:var(--white)}
body{position:relative;font-family:'Noto Sans',sans-serif;color:var(--text)}
a{color:inherit}
.abs{position:absolute}
.top-band{left:0;top:0;width:1200px;height:460px;background:var(--dark)}
.brand{left:123px;top:36px;display:flex;align-items:center}
.brand-mark{width:84px;height:64px;border-radius:50%;background:#cfcfcf;display:flex;align-items:center;justify-content:center;font:700 15px 'Arimo',sans-serif;color:#555}
.site-title{left:233px;top:46px;font:400 30px 'Arimo',sans-serif;color:var(--white)}
.account-links{left:817px;top:62px;font:700 13px 'Arimo',sans-serif;color:var(--white);word-spacing:2px}
.account-links span{margin:0 7px}
.main-nav{left:100px;top:125px;width:1000px;height:50px;background:var(--nav)}
.main-nav ul{list-style:none;position:absolute;left:21px;top:18px;display:flex;font:700 13px 'Arimo',sans-serif;color:var(--white)}
.main-nav li.sep{margin:0 21px}
.search{left:806px;top:14px;width:141px;height:22px;background:var(--white);border:1px solid #555;font:11px 'Arimo',sans-serif;color:#777;padding:4px 7px}
.search-go{left:953px;top:14px;width:26px;height:22px;background:var(--dark);border:1px solid var(--white);color:var(--white);font:700 11px 'Arimo',sans-serif;text-align:center;line-height:20px}
.hero{left:100px;top:175px;width:1000px;height:349px;background:var(--white);border:3px solid var(--frame);border-top:none}
.hero-art{left:90px;top:40px;width:350px;height:275px;border-radius:8px;background:radial-gradient(circle at 60% 35%,#e62222 0 22%,#f0f0f0 23%,#dedede 60%,#ffffff 100%)}
.hero-title{left:502px;top:103px;font:400 27px 'Alfa Slab One',serif;color:var(--red)}
.hero-text{left:504px;top:155px;width:420px;font:14px/24px 'Didact Gothic',sans-serif;color:var(--text)}
.hero-more{left:820px;top:222px;font:14px 'Arimo',sans-serif;color:var(--red)}
.welcome{left:121px;top:549px;width:710px}
.welcome h1{font:700 19px 'Arimo',sans-serif;margin-bottom:9px}
.welcome h1 em{font-style:normal;font-weight:400;color:var(--red)}
.welcome p{font:12px/18px 'Noto Sans',sans-serif}
.welcome .more{display:inline-block;margin-top:11px;font-size:11px;color:var(--red)}
.welcome-edge{left:852px;top:550px;width:6px;height:150px;background:linear-gradient(to right,#e8e8e8,transparent)}
.news{left:101px;top:746px;width:755px;height:62px;background:var(--dark)}
.news h2{position:absolute;left:12px;top:10px;font:400 12px 'Noto Sans',sans-serif;color:var(--white)}
.news .view{position:absolute;right:18px;top:10px;font-size:11px;color:var(--red)}
.news ul{position:absolute;left:12px;top:35px;list-style:none;display:flex;gap:13px;font-size:10px;color:var(--muted)}
.news li{text-decoration:underline}
.values{left:880px;top:552px;width:205px;height:257px;background:var(--panel);font-family:'Noto Sans',sans-serif}
.values span{position:absolute;white-space:nowrap}
.values-art{left:12px;top:144px;width:181px;height:100px;background:linear-gradient(#ffffff 0,#e9f2f8 40%,#4a90c8 70%,#8cc63f 100%)}
.footer{left:0;top:846px;width:1200px;height:255px;background:var(--dark);color:var(--white)}
.footer h3{position:absolute;font:400 14px 'Noto Sans',sans-serif;color:#e0393f}
.quick-links{position:absolute;top:65px;list-style:none;font:12px/28px 'Noto Sans',sans-serif}
.quick-links a{text-decoration:underline}
.divider{position:absolute;top:31px;width:1px;height:191px;background:#111}
.social{position:absolute;left:459px;top:31px;display:flex;gap:10px}
.social span{width:36px;height:36px;border-radius:5px;background:#3d64a8;font:700 7px/36px 'Noto Sans',sans-serif;text-align:center;color:var(--white)}
.buzz{position:absolute;left:461px;top:86px;width:171px;height:36px;border-radius:4px;background:var(--white);font:400 17px/36px 'Noto Sans',sans-serif;color:#3366cc;text-align:center}
.share{position:absolute;left:461px;top:142px;font:14px 'Noto Sans',sans-serif}
.share a{text-decoration:underline}
.field{position:absolute;left:720px;width:169px;height:20px;border-radius:4px;background:var(--field);font:11px/20px 'Noto Sans',sans-serif;color:#888;padding-left:9px}
.submit{position:absolute;left:835px;top:210px;width:54px;height:21px;border-radius:4px;background:var(--field);color:var(--dark);font:12px/21px 'Noto Sans',sans-serif;text-align:center}
.legal{position:absolute;left:976px;font:11px 'Noto Sans',sans-serif}
.legal a{text-decoration:underline}
</style>
</head>
<body>
<div class="abs top-band"></div>

<header>
  <div class="abs brand"><div class="brand-mark">Pravelo</div></div>
  <div class="abs site-title">Online Research Solutions</div>
  <nav class="abs account-links">Login<span>|</span>My Account<span>|</span>Register<span>|</span>Contact</nav>
</header>

<nav class="abs main-nav">
  <ul>
    <li>ALGEMEEN</li><li class="sep">|</li><li>PRODUCTEEN</li><li class="sep">|</li><li>DEMO'S</li><li class="sep">|</li><li>MEDIA</li><li class="sep">|</li><li>REFERENTIES</li><li class="sep">|</li><li>PERSONEEL</li><li class="sep">|</li><li>CONTACT</li>
  </ul>
  <div class="abs search">Search text here..</div>
  <div class="abs search-go">GO</div>
</nav>

<section class="abs hero">
  <div class="abs hero-art" role="img" aria-label="Red puzzle piece labelled Solution lifting out of a white puzzle"></div>
  <h2 class="abs hero-title">Online Research Solutions</h2>
  <p class="abs hero-text">Pravelo is gespecialiseerd in online gegevensverzameling en analyse en is werkzaam voor internationale opdrachtgevers.</p>
  <a class="abs hero-more" href="#">READ MORE &gt;&gt;</a>
</section>

<section class="abs welcome">
  <h1>Welcome to <em>PRAVELO</em></h1>
  <p>Pravelo is gespecialiseerd in online gegevensverzameling en analyse en is werkzaam voor internationale opdrachtgevers.<br>
  Het bedrijf werd opgericht in 1996 en is gevestigd in Havenwijk, een kleine havenplaats boven Amsterdam. Onze produkten zijn ontwikkeld op basis van Q, een krachtige en uitermate flexibele onderzoekstool voor het verzamelen &amp; verwerken van (online) researchgegevens. Q werd ontwikkeld dóór opinieonderzoekers vóór opinieonderzoekers.<br>
  Ons team bestaat uit zowel opinieonderzoekers als programmeurs met vele jaren ervaring op het gebied van opinieonderzoek en met name met online toepassingen daarvoor.</p>
  <a class="more" href="#">read more &gt;&gt;</a>
</section>
<div class="abs welcome-edge"></div>

<section class="abs news">
  <h2>NEWS &amp; EVENTS</h2>
  <a class="view" href="#">View More</a>
  <ul>
    <li>1) Pieter van Damme legt uit waarom hij onderzoek doet bij Pravelo BV..</li>
    <li>2) Pieter van Damme over Q for Grids..</li>
    <li>3) Pieter van Damme over..</li>
  </ul>
</section>

<aside class="abs values">
  <span style="left:14px;top:15px;font-size:13px;color:var(--olive)">Experiance</span>
  <span style="left:89px;top:11px;font-size:17px;color:#8a8a8a">Quality</span>
  <span style="left:14px;top:40px;font-size:24px;color:var(--red)">Capability</span>
  <span style="left:151px;top:51px;font-size:12px;color:#111">Value</span>
  <span style="left:14px;top:86px;font-size:14px;font-weight:700;color:#888">Online</span>
  <span style="left:69px;top:77px;font-size:23px;color:var(--green)">Research</span>
  <span style="left:14px;top:119px;font-size:17px;color:var(--blue)">Solutions</span>
  <div class="abs values-art" role="img" aria-label="Hand placing a blue cube onto a stack of sky and grass cubes"></div>
</aside>

<footer class="abs footer">
  <h3 style="left:125px;top:29px">Quick Links</h3>
  <ul class="quick-links" style="left:127px">
    <li><a href="#">Algemeen </a></li><li><a href="#">Dataverzameling </a></li><li><a href="#">Analyse </a></li><li><a href="#">Datasetpublising </a></li><li><a href="#">Panel: inPolls</a></li>
  </ul>
  <ul class="quick-links" style="left:297px">
    <li><a href="#">Demo's </a></li><li><a href="#">Media </a></li><li><a href="#">Referenties </a></li><li><a href="#">Personeel </a></li><li><a href="#">Contact </a></li>
  </ul>
  <div class="divider" style="left:416px"></div>
  <div class="social"><span>Friendly</span><span>Linkwork</span><span>Chirper</span><span>OurPlace</span></div>
  <div class="buzz">Chatterbox</div>
  <div class="share">+ <a href="#">bookmark &amp; share</a></div>
  <div class="divider" style="left:676px"></div>
  <h3 style="left:720px;top:29px">Quick Contact</h3>
  <div class="field" style="top:59px">Name</div>
  <div class="field" style="top:89px">Email</div>
  <div class="field" style="top:119px">Contact Number</div>
  <div class="field" style="top:149px;height:53px">Message</div>
  <div class="submit">Submit</div>
  <div class="divider" style="left:932px"></div>
  <div class="legal" style="top:28px">© 2010 <a href="#">pravelo.nl</a></div>
  <div class="legal" style="top:52px">All Rights Reserved</div>
  <div class="legal" style="top:116px"><a href="#">Terms &amp; Conditions</a></div>
  <div class="legal" style="top:144px"><a href="#">Privacy Policy</a></div>
  <div class="legal" style="top:172px"><a href="#">Legal Disclaimer</a></div>
</footer>
</body>
</html>
```